Book cover design needed for a book on Criminal Defense Investigation

Title of book:

Courtroom Fact Finding: Principles, Craft, and Techniques

Author Name:

Walter Ray Hollisford

Instructions: I need book cover designed. I need the full front cover completed with title and author name. For the back cover and spine, please only include the background image. The text for the back cover will be added later. The awarded designer will be contracted at a later date to add the text on the spine and back cover.

Trim size: 6 x 9 inches
Will be printed through Brightmarts’ Pressmaker

Industry/Entity Type

Defense

Requirements
Must have
• Instructions: I need book cover designed. I need the full front cover completed with title and author name. I need compelling imagery incorporated into the design. For the back cover and spine, please only include the background image. The text for the back cover will be added later. The awarded designer will be contracted at a later date to add the text on the spine and back cover.

```html
<!DOCTYPE html>
<html lang="en">
<head>
<meta charset="utf-8">
<title>Courtroom Fact Finding — Front Cover</title>
<link href="https://fonts.googleapis.com/css2?family=Inter:ital,wght@0,400;0,500;0,600;1,400&display=swap" rel="stylesheet">
<style>
  :root {
    --coral: #f25a57;
    --paper: #ffffff;
    --ink-red: #f0524f;
    --ink-muted: #e8706c;
  }
  html, body {
    margin: 0;
    padding: 0;
    width: 872px;
    height: 1200px;
    overflow: hidden;
    background: var(--coral);
  }
  .cover {
    position: relative;
    width: 872px;
    height: 1200px;
    background: var(--coral);
    font-family: "Inter", "Helvetica Neue", Arial, sans-serif;
    overflow: hidden;
  }
  .cover__lines {
    position: absolute;
    inset: 0;
  }
  .title-panel {
    position: absolute;
    left: 41px;
    top: 35px;
    width: 787px;
    height: 408px;
    background: var(--paper);
  }
  .title-panel__frame {
    position: absolute;
    inset: 0;
  }
  .title-panel__title {
    position: absolute;
    left: 0;
    right: 0;
    top: 52px;
    margin: 0;
    text-align: center;
    color: var(--ink-red);
    font-weight: 500;
    font-size: 74px;
    line-height: 82px;
    letter-spacing: -0.5px;
  }
  .title-panel__subtitle {
    position: absolute;
    left: 0;
    right: 0;
    top: 292px;
    margin: 0;
    text-align: center;
    color: var(--ink-red);
    font-weight: 400;
    font-size: 29px;
    line-height: 36px;
  }
  .author-tag {
    position: absolute;
    left: 305px;
    top: 471px;
    width: 343px;
    height: 102px;
    background: var(--paper);
    text-align: center;
  }
  .author-tag__name {
    margin: 22px 0 0;
    color: var(--ink-red);
    font-weight: 500;
    font-size: 30px;
    line-height: 36px;
  }
  .author-tag__role {
    margin: 2px 0 0;
    color: var(--ink-muted);
    font-style: italic;
    font-size: 22px;
  }
</style>
</head>
<body>
<main class="cover">
  <svg class="cover__lines" width="872" height="1200" viewBox="0 0 872 1200" aria-hidden="true">
    <g fill="none" stroke="#ffffff" stroke-width="4" stroke-dasharray="20 12">
      <path d="M698 475 A 700 565 0 0 1 0 1040"/>
      <line x1="0" y1="1040" x2="872" y2="1040"/>
      <line x1="0" y1="1082" x2="872" y2="1082"/>
      <line x1="0" y1="1128" x2="872" y2="1128"/>
    </g>
  </svg>

  <section class="title-panel">
    <svg class="title-panel__frame" width="787" height="408" viewBox="0 0 787 408" aria-hidden="true">
      <g fill="none" stroke="#f25a57" stroke-width="4" stroke-dasharray="20 12">
        <rect x="24" y="22" width="739" height="364"/>
        <line x1="150" y1="264" x2="637" y2="264"/>
      </g>
    </svg>
    <h1 class="title-panel__title">Courtroom Fact<br>Finding</h1>
    <p class="title-panel__subtitle">Principles, Craft, and Techniques</p>
  </section>

  <section class="author-tag">
    <p class="author-tag__name">Walter Ray Hollisford</p>
    <p class="author-tag__role">Author</p>
  </section>
</main>
</body>
</html>
```